Popup Nightclub Grand Opening Flyer

We need to design a flyer for the grand opening of an upscale, exclusive nightclub called "Lanternfall". The design needs to be chic and exclusive. The background should be black and the text should primarily be white. We like minimalist designs.

Here is the text for the flyer
-
Velvetrope Atlanta Presents

Lanternfall (LOGO)

A Popup Nightclub Experience
For one night Only

Friday, October 18, 2013
Party begins at 9PM

INVITE ONLY

See invitation for location details
(Velvetrope Atlanta logo)

-
Examples we like

http://cdn2-b.brivelpost.com/sites/default/files/styles/image_content_width/hash/3d/fa/1472093815_4471_flyer.jpg?itok=R8kqWm2z

http://api.plovra.com/files/7Kqq-Tr82XXB3pQzJvmtR5HL2W719E4nbRtC6KLd4HsfM8Y2qTDK-VmjwDoNqLX4QBzTHD9nakRbVx3m-Pfq8htc3MDTWr5p4/2zelSaturdays.jpg

http://quenmar.com/wp-content/uploads/yootheme/widgetkit/gallery/2zel/2zel-gen_vroom4-01.jpg

Hi All, one thing that we are seeing that we don't like is on over emphasis on the phrase "a popup nightclub experience" please don't make this the largest thing on the flyer

Target Market(s)

Target market is 25-35 year olds who are affluent (rich) and like luxury brands

Requirements
Must have
• Dark Background
Nice to have
• Velvetrope Logo on the bottom
Modern text that isn't curvy
Should not have
• Curved text

```html
<!DOCTYPE html>
<html lang="en">
<head>
<meta charset="utf-8">
<title>Lanternfall Nightclub – Popup Flyer</title>
<link rel="stylesheet" href="https://fonts.googleapis.com/css2?family=Jost:wght@300;400&family=Open+Sans:wght@400;700&display=swap">
<style>
  :root {
    --canvas: #ffffff;
    --flyer-black: #0b0b0b;
    --flyer-charcoal: #262626;
    --text-white: #ffffff;
    --text-grey: #8c8c8c;
    --text-silver: #b9b9b9;
    --mark-silver: #c8c8c8;
  }
  html, body {
    margin: 0;
    padding: 0;
    width: 1200px;
    height: 1000px;
    overflow: hidden;
    background: var(--canvas);
  }
  .canvas {
    position: relative;
    width: 1200px;
    height: 1000px;
    background: var(--canvas);
  }
  .flyer {
    position: absolute;
    left: 310px;
    top: 72px;
    width: 606px;
    height: 856px;
    background: var(--flyer-black);
    overflow: hidden;
    font-family: "Open Sans", Arial, sans-serif;
  }
  .flyer__backdrop {
    position: absolute;
    inset: 0;
    background:
      radial-gradient(ellipse 55% 45% at 62% 45%, rgba(70,70,70,0.55), rgba(0,0,0,0) 70%),
      linear-gradient(180deg, var(--flyer-charcoal) 0%, #151515 45%, var(--flyer-black) 100%);
  }
  .line {
    position: absolute;
    left: 0;
    width: 100%;
    margin: 0;
    text-align: center;
    line-height: 1;
    text-transform: uppercase;
    white-space: nowrap;
  }
  .presenter {
    top: 27px;
    font-size: 24px;
    font-weight: 400;
    color: var(--text-silver);
    letter-spacing: 0.01em;
  }
  .brand-mark {
    position: absolute;
    left: 239px;
    top: 80px;
    width: 128px;
    height: 128px;
  }
  .brand-name {
    top: 260px;
    font-family: "Jost", Arial, sans-serif;
    font-weight: 300;
    font-size: 50px;
    letter-spacing: 0.14em;
    color: var(--text-white);
    text-indent: 0.14em;
  }
  .brand-type {
    top: 326px;
    font-family: "Jost", Arial, sans-serif;
    font-weight: 300;
    font-size: 30px;
    letter-spacing: 0.16em;
    color: var(--text-white);
    text-indent: 0.16em;
  }
  .headline {
    top: 474px;
    font-size: 25px;
    font-weight: 700;
    letter-spacing: 0.08em;
    color: var(--text-white);
  }
  .subline {
    font-size: 25px;
    font-weight: 700;
    color: var(--text-grey);
  }
  .subline--night { top: 506px; }
  .event-date {
    top: 574px;
    font-size: 37px;
    font-weight: 700;
    color: var(--text-white);
  }
  .subline--time { top: 616px; }
  .access {
    top: 686px;
    font-size: 25px;
    font-weight: 700;
    color: var(--text-white);
  }
  .location-note {
    top: 733px;
    font-size: 22px;
    font-weight: 700;
    letter-spacing: 0.08em;
    color: var(--text-grey);
  }
  .presenter-sign {
    position: absolute;
    left: 0;
    top: 794px;
    width: 100%;
    display: flex;
    justify-content: center;
    align-items: center;
    gap: 12px;
  }
  .presenter-sign__dot {
    width: 22px;
    height: 22px;
    border-radius: 50%;
    background: var(--text-white);
  }
  .presenter-sign__name {
    font-family: "Open Sans", Arial, sans-serif;
    font-weight: 400;
    font-size: 22px;
    letter-spacing: 0.14em;
    color: var(--text-white);
    text-transform: uppercase;
    line-height: 1;
  }
</style>
</head>
<body>
<main class="canvas">
  <article class="flyer">
    <div class="flyer__backdrop" role="img" aria-label="Faint dark photograph of a dancer in a nightclub"></div>

    <p class="line presenter">Velvetrope Atlanta Presents</p>

    <svg class="brand-mark" viewBox="0 0 128 128" aria-hidden="true">
      <defs>
        <linearGradient id="markSilver" x1="0" y1="0" x2="0" y2="1">
          <stop offset="0" stop-color="#e4e4e4"/>
          <stop offset="1" stop-color="#9a9a9a"/>
        </linearGradient>
      </defs>
      <circle cx="64" cy="64" r="60" fill="url(#markSilver)"/>
    </svg>

    <h1 class="line brand-name">Lanternfall</h1>
    <p class="line brand-type">Nightclub</p>

    <h2 class="line headline">A Popup Nightclub Experience</h2>
    <p class="line subline subline--night">For One Night Only</p>

    <p class="line event-date">Friday, October 18, 2013</p>
    <p class="line subline subline--time">Party Begins at 9PM</p>

    <p class="line access">Invite Only</p>
    <p class="line location-note">See Invitation for Location Details</p>

    <footer class="presenter-sign">
      <span class="presenter-sign__dot" aria-hidden="true"></span>
      <span class="presenter-sign__name">Velvetrope Atlanta</span>
    </footer>
  </article>
</main>
</body>
</html>
```